Pages toward Inner Calm - book cover

12/18 update: Please read the entire brief. I don’t love anything that has been provided up to today. Please use the graphics and colors I’ve attached!!!! Show me your creations.

I am looking for a book cover design. It is a mental health journal. Needs to be very warm, inviting, calming. I’m very interested in new creative ideas. It will be wire-o bound and also in hard copy front and back. Use the graphic and colors I already have attached to this file. It’s called “Pages Toward Inner Calm”. Self means soul or spirit or center. The idea of integration may be a fit here in some way. If some words need to be emphasized in the design, “Self” and “QRM” would be the most important. size 6"x9". The words on the front can be smaller and more inviting then they would normally be on a fiction paperback.

Update 12/16: I am not excited about any of the submissions so far. I’m looking forward to seeing more options.

Target Market(s)

Adults 30-60. Male and female. People who like to learn. People wanting to heal. Middle and upper income.

Industry/Entity Type

Mental health. Wellness

Font styles to use
Other font styles liked:
• Whatever font is used in my logo. i don’t know the name. I also would be open to a different font if it was warm, inviting, and calm.

Colors
0094D4
00A9DD
6FCCEA
C7EBF8
E9F6FB

Requirements
Must have
• My logo colors. The words “Pages Toward Inner Calm” and “A 13-Week QRM Exploration”
Nice to have
• I’d like to see some creative ideas. More abstract than realistic.
Should not have
• No realist art or photos.

```html
<!DOCTYPE html>
<html lang="en">
<head>
<meta charset="utf-8">
<title>Pages toward Inner Calm – Cover Spread</title>
<link rel="stylesheet" href="https://fonts.googleapis.com/css2?family=Cormorant+Garamond:wght@500;600&family=Lora:wght@400&display=swap">
<style>
  :root {
    --teal-deep: #163c46;
    --teal-mid: #134653;
    --teal-light: #1b5766;
    --band-dark: rgba(13, 42, 50, 0.55);
    --band-darker: rgba(12, 38, 46, 0.88);
    --ink: #ffffff;
    --title-serif: "Cormorant Garamond", Georgia, serif;
    --text-serif: "Lora", Georgia, serif;
  }
  * { margin: 0; padding: 0; box-sizing: border-box; }
  html, body { width: 1200px; height: 826px; overflow: hidden; background: var(--teal-deep); }
  .spread { position: relative; width: 1200px; height: 826px; color: var(--ink); font-family: var(--text-serif); }
  .panel { position: absolute; top: 0; height: 826px; overflow: hidden; }
  .panel--back { left: 0; width: 584px; }
  .panel--spine { left: 584px; width: 31px; border-left: 1.5px solid var(--ink); border-right: 1.5px solid var(--ink); background: var(--teal-deep); }
  .panel--front { left: 615px; width: 585px; }

  .backdrop {
    position: absolute; inset: 0;
    background:
      linear-gradient(150deg, var(--teal-deep) 0%, var(--teal-mid) 30%, var(--teal-deep) 48%, var(--teal-light) 62%, var(--teal-mid) 74%, var(--teal-deep) 100%);
  }
  .mid-band { position: absolute; left: 0; right: 0; top: 274px; height: 245px; background: var(--band-dark); }

  .title { position: absolute; left: 0; right: 0; text-align: center; font-family: var(--title-serif); font-weight: 600; line-height: 1; }
  .title__main { display: block; letter-spacing: -0.03em; }
  .title__sub { display: block; font-weight: 500; letter-spacing: 0; }
  .panel--back .title { top: 80px; }
  .panel--back .title__main { font-size: 48px; }
  .panel--back .title__sub { font-size: 22px; margin-top: 0; }
  .panel--front .title { top: 340px; }
  .panel--front .title__main { font-size: 84px; }
  .panel--front .title__sub { font-size: 36px; margin-top: 2px; }

  .brand { position: absolute; left: 0; right: 0; text-align: center; font-family: var(--text-serif); font-size: 12px; letter-spacing: 0.34em; line-height: 1.7; }
  .brand__dot { display: block; width: 44px; height: 44px; margin: 0 auto 10px; border: 1px solid var(--ink); border-radius: 50%; }
  .panel--back .brand { top: 352px; left: 28px; }
  .panel--front .brand { top: 90px; }

  .website { position: absolute; left: 0; right: 0; top: 738px; text-align: center; font-size: 15px; letter-spacing: 0.02em; padding-left: 28px; }

  .subtitle-band { position: absolute; left: 0; right: 0; top: 719px; height: 47px; background: var(--band-darker); }
  .subtitle { position: absolute; left: 0; right: 0; top: 725px; text-align: center; font-size: 26px; line-height: 34px; }

  .spine-text {
    position: absolute; left: 0; width: 28px;
    writing-mode: vertical-rl; transform: rotate(180deg);
    white-space: nowrap; font-size: 15.5px; line-height: 28px; text-align: start;
  }
  .spine-text--subtitle { top: 262px; height: 205px; }
  .spine-text--title { top: 508px; height: 185px; }
  .spine-rule { position: absolute; left: 8px; top: 496px; width: 11px; height: 1px; background: var(--ink); }
</style>
</head>
<body>
<main class="spread">
  <section class="panel panel--back">
    <div class="backdrop" role="img" aria-label="Abstract flowing teal wave background"></div>
    <div class="mid-band"></div>
    <h2 class="title"><span class="title__main">PAGES</span><span class="title__sub">TOWARD INNER CALM</span></h2>
    <div class="brand"><span class="brand__dot"></span>LINDQVIST<br>WELLNESS</div>
    <p class="website">www.lindqvistwellness.com</p>
  </section>

  <section class="panel panel--spine">
    <span class="spine-text spine-text--subtitle">A 13-Week QRM Exploration</span>
    <span class="spine-rule"></span>
    <span class="spine-text spine-text--title">Pages Toward Inner Calm</span>
  </section>

  <section class="panel panel--front">
    <div class="backdrop" role="img" aria-label="Abstract flowing teal wave background"></div>
    <div class="mid-band"></div>
    <div class="brand"><span class="brand__dot"></span>LINDQVIST<br>WELLNESS</div>
    <h1 class="title"><span class="title__main">PAGES</span><span class="title__sub">TOWARD INNER CALM</span></h1>
    <div class="subtitle-band"></div>
    <p class="subtitle">A 13-Week QRM Exploration</p>
  </section>
</main>
</body>
</html>
```